Postcard Design

We need a postcard design for a private lender in the Denver area. We are offering hard money loans and loans for those doing fix-and-flips. We definitely want something that is Colorado-specific, maybe a view of downtown Denver? We are not offering small personal loans, but we are also not lending over 800k. Our audience is not major corporations. all the info in the old postcard is correct EXCEPT:

the new email should be thimble417@postvane.net

We would like to omit all use of exclamation points.

```html
<!DOCTYPE html>
<html lang="en">
<head>
<meta charset="utf-8">
<title>Kestrel Lending Postcard</title>
<link rel="stylesheet" href="https://fonts.googleapis.com/css2?family=Cinzel:wght@400;600&family=Cabin+Condensed:wght@700&family=Ubuntu:wght@700&family=Arimo:wght@700&family=Tinos&family=Marcellus&family=Archivo+Black&family=Oswald:wght@600&display=swap">
<style>
  :root {
    --page: #ffffff;
    --header-top: #2fa3dc;
    --header-bottom: #1d5fa0;
    --panel-blue: #4a7fb6;
    --panel-blue-dark: #2f5f92;
    --cream: #eef0cf;
    --rate-red: #c0272d;
    --band-green: #1f7a34;
    --band-green-dark: #0f5a22;
    --notice-yellow: #f1e51e;
    --box-red: #a52a1e;
    --box-red-dark: #7f1e14;
    --phone-yellow: #f4e01c;
    --contact-blue: #2a55a8;
    --contact-blue-dark: #1b3576;
    --strip-dark: #2d3a4c;
    --back-grey: #ececec;
    --slate: #3d5068;
    --slate-dark: #1e2c3e;
    --slogan-red: #c5262a;
    --shadow: rgba(0,0,0,0.45);
  }
  * { margin: 0; padding: 0; box-sizing: border-box; }
  html, body { width: 1200px; height: 1200px; overflow: hidden; background: var(--page); }
  .canvas { position: relative; width: 1200px; height: 1200px; }

  .card-front {
    position: absolute; left: 204px; top: 0; width: 772px; height: 592px;
    box-shadow: 6px 6px 6px var(--shadow);
  }
  .front-header {
    position: absolute; left: 0; top: 0; width: 100%; height: 74px;
    background: linear-gradient(180deg, var(--header-top), var(--header-bottom));
    display: flex; align-items: center; justify-content: center;
    font-family: "Cinzel", serif; font-weight: 600; font-size: 36px; color: #fff;
    letter-spacing: 1px; text-shadow: 1px 2px 2px rgba(0,0,0,0.5);
  }
  .services-panel {
    position: absolute; left: 0; top: 74px; width: 396px; height: 340px;
    background: radial-gradient(ellipse at 50% 40%, var(--panel-blue), var(--panel-blue-dark));
    text-align: center; color: #fff;
    font-family: "Cabin Condensed", sans-serif; font-weight: 700;
    text-shadow: 2px 2px 2px rgba(0,0,0,0.7);
  }
  .handshake-art {
    position: absolute; left: 102px; top: 6px; width: 194px; height: 84px;
    background: linear-gradient(90deg, #37506d, #2b3f57);
    border-radius: 6px;
  }
  .services-panel p {
    position: absolute; left: 0; width: 100%;
    font-size: 27px; line-height: 27px; letter-spacing: 0.6px;
  }
  .services-panel .line-one { top: 100px; }
  .services-panel .line-two { top: 154px; }
  .services-panel .line-three { top: 208px; }

  .rates-panel {
    position: absolute; left: 396px; top: 74px; width: 376px; height: 340px;
    background: linear-gradient(180deg, var(--cream) 0%, #d9dcc0 55%, #8a8478 100%);
  }
  .skyline-photo {
    position: absolute; left: 0; top: 100px; width: 100%; height: 240px;
    background: linear-gradient(180deg, rgba(200,190,170,0) 0%, #a89a8c 45%, #5b4a44 100%);
  }
  .rates-panel h2 {
    position: absolute; left: 0; width: 100%; text-align: center;
    font-family: "Ubuntu", sans-serif; font-weight: 700; color: var(--rate-red);
  }
  .rates-panel .rate-main { top: 24px; font-size: 29px; }
  .rates-panel .rate-flip { top: 70px; font-size: 24px; }
  .rates-panel .closing {
    top: 108px; left: -24px; font-family: "Oswald", sans-serif; font-weight: 600; font-size: 24px;
  }

  .offer-band {
    position: absolute; left: 0; top: 414px; width: 100%; height: 134px;
    background: linear-gradient(90deg, var(--band-green-dark), var(--band-green) 50%, var(--band-green-dark));
  }
  .offer-band .fees {
    position: absolute; left: 32px; top: 6px;
    font-family: "Ubuntu", sans-serif; font-weight: 700; font-size: 22px; color: var(--notice-yellow);
  }
  .lender-box {
    position: absolute; left: 30px; top: 44px; width: 688px; height: 68px;
    background: linear-gradient(180deg, var(--box-red), var(--box-red-dark));
    border: 1px solid #c8563f; box-shadow: 3px 3px 4px rgba(0,0,0,0.5);
    font-family: "Arimo", sans-serif; font-weight: 700; color: #fff; font-size: 20px;
    padding: 11px 0 0 30px; line-height: 28px;
  }
  .lender-box .phone { color: var(--phone-yellow); font-size: 23px; margin-left: 10px; }

  .contact-strip {
    position: absolute; left: 0; top: 548px; width: 100%; height: 44px;
    background: var(--strip-dark);
  }
  .contact-box {
    position: absolute; left: 396px; top: 0; width: 376px; height: 44px;
    background: linear-gradient(90deg, var(--contact-blue), var(--contact-blue-dark));
    font-family: "Tinos", serif; color: #fff; font-size: 17px; line-height: 19px;
    padding: 5px 0 0 20px;
  }

  .card-back {
    position: absolute; left: 202px; top: 604px; width: 774px; height: 596px;
    background: var(--back-grey);
    box-shadow: 4px 0 5px var(--shadow);
  }
  .return-panel {
    position: absolute; left: 0; top: 0; width: 376px; height: 494px;
    background: radial-gradient(ellipse at 45% 55%, var(--slate) 0%, var(--slate) 40%, var(--slate-dark) 100%);
    box-shadow: 9px 14px 0 #8e8888;
  }
  .return-address {
    position: absolute; left: 0; top: 36px; width: 100%; text-align: center;
    font-family: "Marcellus", serif; font-size: 27px; line-height: 28px; color: #fff;
  }
  .slogan-line {
    position: absolute; width: 400px; text-align: center; white-space: nowrap;
    transform: rotate(-15deg); transform-origin: center;
    font-family: "Archivo Black", sans-serif; color: #fff;
    text-shadow: 2px 3px 2px rgba(0,0,0,0.7);
  }
  .slogan-low { left: -34px; top: 202px; font-size: 30px; line-height: 40px; }
  .slogan-hard { left: -21px; top: 248px; font-size: 41px; line-height: 52px; color: var(--slogan-red); }
  .slogan-loans { left: -6px; top: 318px; font-size: 29px; line-height: 40px; }
  .stamp-box {
    position: absolute; left: 620px; top: 34px; width: 112px; height: 128px; background: #fff;
  }
</style>
</head>
<body>
<div class="canvas">
  <section class="card-front">
    <header class="front-header">KESTREL LENDING INC.</header>

    <div class="services-panel">
      <div class="handshake-art" role="img" aria-label="Illustration of two hands in a handshake"></div>
      <p class="line-one">Hard money loans</p>
      <p class="line-two">We are loaning our own funds</p>
      <p class="line-three">We do a variety of real estate<br>secured loans including loans<br>to buy foreclosures,<br>short sales &amp; more</p>
    </div>

    <div class="rates-panel">
      <div class="skyline-photo" role="img" aria-label="Photo of the downtown Denver skyline"></div>
      <h2 class="rate-main">LOAN RATES FROM 8 %</h2>
      <h2 class="rate-flip">FIX &amp; FLIP LOANS AT 10 %</h2>
      <h2 class="closing">FAST CLOSING</h2>
    </div>

    <div class="offer-band">
      <p class="fees">No appraisal, processing fees or "junk" fees</p>
      <div class="lender-box">
        DENVER PRIVATE MONEY LENDER<br>
        PRIVATE MONEY FOR LESS- CALL US AT<span class="phone">303-555-0147</span>
      </div>
    </div>

    <div class="contact-strip">
      <div class="contact-box">
        thimble417@postvane.net<br>
        http://kestrellendinginc.com
      </div>
    </div>
  </section>

  <section class="card-back">
    <div class="return-panel">
      <p class="return-address">KESTREL LENDING, INC.<br>1948 Alder St<br>Denver, CO 80202</p>
      <p class="slogan-line slogan-low">LOW COST</p>
      <p class="slogan-line slogan-hard">HARD MONEY</p>
      <p class="slogan-line slogan-loans">REAL STATE LOANS</p>
    </div>
    <div class="stamp-box"></div>
  </section>
</div>
</body>
</html>
```